Amber Ridge Publishing Web Page Design

Design a website for my new start up publishing company - Amber Ridge Publishing, the first work published by ARP with be a new book by M.R. Theodor called Silent Ledger. The prototype for the book cover is attached.

Target Market(s)

Worldwide, all readers of mystery, fiction, etc.

Industry/Entity Type

Book Publisher

Coding

Coded - Design and coding required

Number of Pages Required

1 page

```html
<!DOCTYPE html>
<html lang="en">
<head>
<meta charset="utf-8">
<title>Amber Ridge Publishing</title>
<link rel="stylesheet" href="https://fonts.googleapis.com/css2?family=Lato:wght@400;700&family=Tinos:wght@700&family=Arimo&family=Oswald:wght@500&display=swap">
<style>
:root{
  --ink:#222;
  --nav:#444;
  --red:#e8380d;
  --tag:#ff4a3a;
  --crimson:#c0190f;
  --blue:#0a6fd0;
  --navy:#2c5895;
  --navy-dark:#244a80;
  --gold:#f6c21c;
  --teal:#38c6d8;
  --grey:#eaeaea;
  --light:#f4f4f4;
  --white:#fff;
}
*{box-sizing:border-box;margin:0;padding:0}
html,body{width:1200px;height:3522px;overflow:hidden}
body{font-family:"Lato",sans-serif;color:var(--ink);background:var(--white);position:relative}
.abs{position:absolute}

/* header */
.brand{left:78px;top:22px;font-family:"Arimo",sans-serif;font-size:27px;color:#111}
.brand b{color:var(--red);font-weight:400}
.social{top:26px;right:106px;display:flex;gap:16px}
.social span{width:14px;height:14px;border-radius:50%;background:var(--red);display:block}
.nav{top:84px;left:0;width:1200px;font-size:13px;color:var(--nav);text-transform:uppercase}
.nav a{position:absolute;color:inherit;text-decoration:none;white-space:nowrap}
.caret{display:inline-block;border:4px solid transparent;border-top-color:var(--nav);margin-left:6px;vertical-align:-1px}

/* hero */
.hero{left:0;top:108px;width:1200px;height:609px;
  background:
    linear-gradient(to top,rgba(8,8,20,.95) 0%,rgba(14,12,34,.75) 14%,rgba(0,0,0,0) 34%),
    radial-gradient(ellipse 520px 360px at 58% 28%,#b7a2f4 0%,#7b60d4 20%,#3e2f8e 48%,rgba(20,16,60,0) 80%),
    linear-gradient(#1a1440,#0e0c28)}
.hero-ridge{left:0;top:600px;width:1200px;height:117px}
.search{left:298px;top:190px;width:530px;height:38px;background:var(--white);border:2px solid var(--white);display:flex}
.search .field{flex:1;font-size:12px;color:#999;padding:10px 0 0 40px;position:relative}
.search svg{position:absolute;left:10px;top:10px}
.search .btn{width:106px;background:var(--red);color:var(--white);font-size:15px;font-weight:700;text-align:center;line-height:34px}

.book3d{left:148px;top:278px;width:250px;height:374px;transform:skewY(-3deg);filter:drop-shadow(10px 12px 12px rgba(0,0,0,.55))}
.book3d .pages{position:absolute;right:0;top:6px;width:14px;height:362px;background:linear-gradient(90deg,#cfcfcf,#f4f4f4 40%,#bdbdbd)}
.book3d .front{position:absolute;left:0;top:0;width:238px;height:374px;
  background:
    linear-gradient(100deg,rgba(255,255,255,.14) 0,rgba(255,255,255,0) 8%),
    radial-gradient(ellipse 90px 200px at 60% 70%,rgba(150,170,255,.45),rgba(0,0,0,0) 70%),
    linear-gradient(165deg,#24358a 0%,#121a52 45%,#070a22 100%);
  border-left:4px solid #0a0f30}
.book3d .t{position:absolute;left:22px;top:34px;width:200px;font-family:"Oswald",sans-serif;font-weight:500;font-size:46px;line-height:46px;color:var(--gold);text-align:center;text-shadow:2px 2px 0 #6b2a00}
.book3d .a{position:absolute;left:0;bottom:24px;width:238px;text-align:center;font-family:"Oswald",sans-serif;font-size:26px;color:var(--teal);letter-spacing:1px}

.hero-title{left:482px;top:316px;font-family:"Tinos",serif;font-weight:700;font-size:55px;color:var(--gold);letter-spacing:1px;line-height:60px}
.hero-tag{left:482px;top:396px;font-family:"Tinos",serif;font-weight:700;font-size:14px;color:var(--tag);line-height:17px;text-shadow:0 1px 3px rgba(0,0,0,.85)}
.hero-by{left:482px;top:444px;font-family:"Tinos",serif;font-weight:700;font-size:14px;color:var(--white)}
.learn{left:477px;top:495px;width:139px;height:42px;background:var(--red);color:var(--white);font-size:17px;text-align:center;line-height:42px;border-radius:2px}

/* connect */
.h2{left:0;width:1200px;text-align:center;font-size:24px;font-weight:400;text-transform:uppercase}
.connect{top:770px;color:#333}
.c-item{top:842px;width:140px;text-align:center;font-size:11.5px;color:#333;line-height:17px}
.c-item .ico{width:40px;height:40px;margin:0 auto 10px}
.tabs{left:100px;top:1018px;width:1000px;height:36px;display:flex;gap:3px}
.tabs div{flex:1;background:var(--grey);font-size:12.5px;font-weight:700;text-align:center;line-height:36px;text-transform:uppercase}
.tabs .on{background:var(--blue);color:var(--white)}
.book{top:1082px;width:193px;height:296px;box-shadow:0 1px 3px rgba(0,0,0,.2)}
.arrow{top:1215px;width:18px;height:40px}

/* authors */
.authors{left:0;top:1440px;width:1200px;height:666px;background:var(--blue)}
.authors .h2{color:var(--white);top:30px;font-size:23px}
.face{width:210px;height:228px}
.az{left:547px;top:610px;width:105px;height:34px;border:1px solid var(--white);color:var(--white);font-size:13px;text-align:center;line-height:32px}

/* newsletter */
.news{left:0;top:2106px;width:1200px;height:193px;background:var(--crimson);color:var(--white)}
.news h3{position:absolute;left:99px;top:28px;font-weight:400;font-size:19px}
.news p{position:absolute;left:99px;top:68px;width:520px;font-size:14px;line-height:21px}
.news small{position:absolute;left:99px;top:140px;font-size:10px;color:#ffd2cc}
.news .in{position:absolute;left:699px;width:402px;height:34px;background:var(--white);color:#777;font-size:11px;padding:10px 8px}
.news .sub{position:absolute;left:699px;top:137px;width:98px;height:25px;background:#1a2233;font-size:12px;text-align:center;line-height:25px}

/* instagram */
.insta{top:2332px;color:#333}
.tile{width:239px;height:240px}
.credit{left:925px;top:2884px;font-size:8px;letter-spacing:1px;color:#888}
.mini{left:128px;top:2888px;width:26px;height:26px;border-radius:50%;background:var(--white);box-shadow:0 1px 4px rgba(0,0,0,.25)}

/* imprints */
.imprints{left:0;top:2986px;width:1200px;height:141px;background:var(--light)}
.imp{top:62px;width:126px;text-align:center;font-size:11px;font-weight:700;color:#333;text-transform:uppercase;letter-spacing:.5px}

/* footer */
.footer{left:0;top:3127px;width:1200px;height:344px;background:var(--navy);color:var(--white)}
.footer h4{position:absolute;left:102px;top:25px;font-weight:400;font-size:17px}
.footer .about{position:absolute;left:97px;top:68px;width:482px;font-size:11px;line-height:16.5px}
.footer ul{position:absolute;left:716px;top:68px;list-style:none;font-size:11px;line-height:22.8px}
.footer address{position:absolute;left:918px;top:64px;font-style:normal;font-size:11px;line-height:16.5px}
.f-social{position:absolute;left:107px;top:282px;display:flex;gap:19px}
.f-social span{width:14px;height:14px;border-radius:50%;background:var(--white);display:block}
.bottom{left:0;top:3471px;width:1200px;height:51px;background:var(--navy-dark);color:#dfe7f3;font-size:11px}
.bottom div{position:absolute;right:104px;top:26px;word-spacing:4px}
.totop{right:14px;top:3468px;width:46px;height:46px;border-radius:50%;background:#2f66b0}
</style>
</head>
<body>

<header>
  <div class="abs brand">Amber Ridge <b>ARP</b></div>
  <div class="abs social" aria-label="Social links"><span></span><span></span><span></span><span></span><span></span></div>
  <nav class="abs nav">
    <a style="left:139px">Books<i class="caret"></i></a>
    <a style="left:245px">Authors</a>
    <a style="left:353px">Ridge Broadcast<i class="caret"></i></a>
    <a style="left:548px">Book Finder</a>
    <a style="left:683px">Contact Us</a>
    <a style="left:820px">Publish With Us</a>
  </nav>
</header>

<section class="abs hero" role="img" aria-label="Stormy violet night sky lit by lightning over dark mountains"></section>
<svg class="abs hero-ridge" viewBox="0 0 1200 117" preserveAspectRatio="none" aria-hidden="true"><path d="M0 70 C120 40 220 60 330 30 C430 5 520 50 640 20 C760 -5 860 45 980 25 C1080 10 1150 40 1200 30 L1200 117 L0 117 Z" fill="#0a0a1a" opacity=".85"/></svg>

<div class="abs search">
  <div class="field"><svg width="14" height="14" viewBox="0 0 14 14"><circle cx="6" cy="6" r="4.5" fill="none" stroke="#555" stroke-width="1.6"/><line x1="9.3" y1="9.3" x2="13" y2="13" stroke="#555" stroke-width="1.8"/></svg>Search by Title or Author</div>
  <div class="btn">Search</div>
</div>

<div class="abs book3d" role="img" aria-label="Silent Ledger hardcover by M.R. Theodor, lightning over a construction site">
  <div class="pages"></div>
  <div class="front">
    <div class="t">SILENT<br>LEDGER</div>
    <div class="a">M.R. THEODOR</div>
  </div>
</div>

<h1 class="abs hero-title">SILENT LEDGER</h1>
<p class="abs hero-tag">MURDER,CONSPIRACY,CHANGE ORDERS<br>THE CONSTRUCTION BUSINESS CAN BE A KILLER</p>
<p class="abs hero-by">BY M.R. THEODOR</p>
<div class="abs learn">Learn More</div>

<h2 class="abs h2 connect">Connect</h2>
<div class="abs c-item" style="left:101px"><div class="ico"><svg width="40" height="40"><circle cx="18" cy="11" r="8" fill="#1e6fcf"/><rect x="6" y="21" width="24" height="15" rx="6" fill="#1e6fcf"/><rect x="30" y="26" width="8" height="8" fill="#e8380d"/></svg></div>Are you an aspiring<br>author?</div>
<div class="abs c-item" style="left:244px"><div class="ico"><svg width="40" height="40"><rect x="3" y="3" width="26" height="20" fill="none" stroke="#e8380d" stroke-width="3"/><circle cx="28" cy="22" r="5" fill="#1e6fcf"/><rect x="22" y="28" width="12" height="10" fill="#1e6fcf"/></svg></div>Are you an educator?</div>
<div class="abs c-item" style="left:387px"><div class="ico"><svg width="40" height="40"><rect x="2" y="24" width="36" height="10" fill="#e8380d"/><rect x="6" y="14" width="6" height="10" fill="#1e6fcf"/><circle cx="24" cy="12" r="5" fill="#1e6fcf"/><rect x="19" y="18" width="10" height="6" fill="#1e6fcf"/></svg></div>Are you a<br>librarian?</div>
<div class="abs c-item" style="left:530px"><div class="ico"><svg width="40" height="40"><rect x="6" y="4" width="28" height="7" fill="#1e6fcf"/><rect x="4" y="13" width="32" height="7" fill="#e8380d"/><rect x="6" y="22" width="28" height="7" fill="#1e6fcf"/><rect x="4" y="31" width="32" height="7" fill="#e8380d"/></svg></div>Are you a<br>book club?</div>
<div class="abs c-item" style="left:672px"><div class="ico"><svg width="40" height="40"><rect x="5" y="4" width="28" height="32" fill="none" stroke="#1e6fcf" stroke-width="3"/><line x1="10" y1="14" x2="27" y2="14" stroke="#1e6fcf" stroke-width="2"/><line x1="10" y1="21" x2="22" y2="21" stroke="#1e6fcf" stroke-width="2"/><line x1="22" y1="30" x2="37" y2="12" stroke="#e8380d" stroke-width="3"/></svg></div>Are you a<br>blogger?</div>
<div class="abs c-item" style="left:815px"><div class="ico"><svg width="40" height="40"><circle cx="18" cy="11" r="8" fill="#1e6fcf"/><rect x="6" y="21" width="24" height="15" rx="6" fill="#1e6fcf"/><circle cx="33" cy="31" r="6" fill="#e8380d"/></svg></div>Do you want to be a<br>part of our guest list?</div>
<div class="abs c-item" style="left:959px"><div class="ico"><svg width="40" height="40"><circle cx="20" cy="20" r="17" fill="none" stroke="#e8380d" stroke-width="2"/><circle cx="20" cy="16" r="6" fill="#1e6fcf"/><rect x="11" y="24" width="18" height="8" rx="4" fill="#1e6fcf"/></svg></div>Do you want to<br>collaborate?</div>

<div class="abs tabs"><div class="on">Just Released</div><div>Trending Now</div><div>Coming Soon</div><div>Award Winners</div></div>
<svg class="abs arrow" style="left:72px" viewBox="0 0 18 40"><polyline points="15,3 3,20 15,37" fill="none" stroke="#ccc" stroke-width="2"/></svg>
<div class="abs book" style="left:100px;background:linear-gradient(#f2f3f5 0%,#d9dcde 30%,#f4f2ee 45%,#e2ddd4 100%)" role="img" aria-label="Book cover with a snowy village scene and grey title lettering"></div>
<div class="abs book" style="left:302px;background:linear-gradient(160deg,#f6d41c 0%,#f0a21c 35%,#e2245e 70%,#b8124a 100%)" role="img" aria-label="Book cover with bold yellow film-poster lettering on pink"></div>
<div class="abs book" style="left:504px;background:linear-gradient(120deg,#c4181c 0%,#9a1216 50%,#e8e0dc 52%,#7a0c0e 56%,#6e0c0e 100%)" role="img" aria-label="Book cover with a knife blade on red"></div>
<div class="abs book" style="left:706px;height:304px;background:radial-gradient(ellipse at 50% 35%,#5a5a5a 0%,#2a2a2a 45%,#111 100%)" role="img" aria-label="Fitness book cover with an athlete lifting weights"></div>
<div class="abs book" style="left:908px;background:radial-gradient(ellipse at 50% 45%,#2fc6d8 0%,#12b2c6 55%,#0a98ad 100%)" role="img" aria-label="Book cover with a line drawing of a masked figure on teal"></div>
<svg class="abs arrow" style="left:1108px" viewBox="0 0 18 40"><polyline points="3,3 15,20 3,37" fill="none" stroke="#ccc" stroke-width="2"/></svg>

<section class="abs authors">
  <h2 class="abs h2">Meet Our Authors</h2>
  <div class="abs face" style="left:144px;top:91px;background:radial-gradient(ellipse at 50% 40%,#d8a88a 0%,#8a6a56 40%,#3d4d68 100%)" role="img" aria-label="Author portrait"></div>
  <div class="abs face" style="left:372px;top:91px;background:radial-gradient(ellipse at 50% 45%,#c08a74 0%,#5a4a6a 45%,#24202c 100%)" role="img" aria-label="Author portrait"></div>
  <div class="abs face" style="left:600px;top:91px;background:radial-gradient(ellipse at 50% 40%,#e0b49a 0%,#8a6a50 45%,#38302c 100%)" role="img" aria-label="Author portrait"></div>
  <div class="abs face" style="left:828px;top:91px;background:radial-gradient(ellipse at 55% 45%,#8c8c8c 0%,#d6d6d6 45%,#fafafa 100%)" role="img" aria-label="Author portrait illustration in greyscale"></div>
  <div class="abs face" style="left:144px;top:338px;background:radial-gradient(ellipse at 50% 40%,#d8a488 0%,#6a5038 45%,#1c1c24 100%)" role="img" aria-label="Author portrait"></div>
  <div class="abs face" style="left:372px;top:338px;background:radial-gradient(ellipse at 50% 40%,#b88a6a 0%,#d2cf9a 50%,#e6e0b8 100%)" role="img" aria-label="Author portrait"></div>
  <div class="abs face" style="left:600px;top:338px;background:radial-gradient(ellipse at 50% 40%,#e4c4b0 0%,#a8b0ba 45%,#3f4956 100%)" role="img" aria-label="Author portrait"></div>
  <div class="abs face" style="left:828px;top:338px;background:radial-gradient(ellipse at 50% 40%,#c89a7a 0%,#8c7e6c 45%,#2f2a26 100%)" role="img" aria-label="Author portrait outdoors"></div>
  <div class="abs az">Authors A-Z</div>
</section>

<section class="abs news">
  <h3>Subscribe to our Newsletter</h3>
  <p>If you love reading and are always on the lookout for the next good read, Ridge Broadcast is THE newsletter you need to check out every month.</p>
  <small>When: On the 30th of every month (around the same time as payday!)</small>
  <div class="in" style="top:31px">First Name*</div>
  <div class="in" style="top:84px">E-mail ID*</div>
  <div class="sub">SUBSCRIBE</div>
</section>

<h2 class="abs h2 insta">Shop Our Instagram</h2>
<div class="abs tile" style="left:108px;top:2386px;background:radial-gradient(ellipse at 50% 55%,#e0a43a 0%,#9a6a2c 40%,#4a3c30 100%)" role="img" aria-label="Book photo on wooden logs"></div>
<div class="abs tile" style="left:357px;top:2386px;background:radial-gradient(ellipse at 50% 60%,#2c4a56 0%,#8a7a70 45%,#ece8e0 100%)" role="img" aria-label="Book photo with illustrated riders"></div>
<div class="abs tile" style="left:605px;top:2386px;background:radial-gradient(ellipse at 55% 50%,#d8c4b0 0%,#9a8878 45%,#4a4440 100%)" role="img" aria-label="Book photo in monochrome"></div>
<div class="abs tile" style="left:853px;top:2386px;background:radial-gradient(ellipse at 45% 40%,#d84a30 0%,#a85040 40%,#8a8a80 100%)" role="img" aria-label="Book photo on stone"></div>
<div class="abs tile" style="left:108px;top:2635px;background:radial-gradient(ellipse at 45% 45%,#4aa05a 0%,#9cc08a 40%,#e6e1d6 100%)" role="img" aria-label="Green book photo on linen"></div>
<div class="abs tile" style="left:357px;top:2635px;background:linear-gradient(120deg,#1b2a6a 0%,#2a3a8a 45%,#d8285a 55%,#a8184a 100%)" role="img" aria-label="Two colourful books"></div>
<div class="abs tile" style="left:605px;top:2635px;background:radial-gradient(ellipse at 60% 100%,#f0b060 0%,#a86a2a 30%,#2c3a5a 75%)" role="img" aria-label="Book photo by lamplight"></div>
<div class="abs tile" style="left:853px;top:2635px;background:linear-gradient(100deg,#4a2a22 0%,#8a3a2a 30%,#e4e0d8 60%,#cfc8bc 100%)" role="img" aria-label="Books on a shelf"></div>
<div class="abs mini"></div>
<div class="abs credit">INSTAGRAM SHOP BY PIXELSHELF</div>

<section class="abs imprints" aria-label="Imprints">
  <div class="abs imp" style="left:100px">Ridge Press</div>
  <div class="abs imp" style="left:224px">Fourth Shelf</div>
  <div class="abs imp" style="left:348px">Ridge Noir</div>
  <div class="abs imp" style="left:474px">Ridge Business</div>
  <div class="abs imp" style="left:599px">Ridge Bhasha</div>
  <div class="abs imp" style="left:724px">Ridge Classics</div>
  <div class="abs imp" style="left:850px">Ridge Sport</div>
  <div class="abs imp" style="left:975px">Ridge Press</div>
</section>

<footer class="abs footer">
  <h4>Amber Ridge Publishing</h4>
  <p class="about">But I must explain to you how all this mistaken idea of denouncing pleasure and praising pain was born and I will give you a complete account of the system, and expound the actual teachings of the great explorer of the truth, the master-builder of human happiness. No one rejects, dislikes, or avoids pleasure itself, because it is pleasure, but because those who do not know how to pursue pleasure rationally encounter consequences that are extremely painful. Nor again is there anyone who loves or pursues or desires to obtain pain of itself, because it is pain, but because occasionally circumstances occur in which toil and pain can procure him some great pleasure. To take a trivial example</p>
  <ul><li>About Us</li><li>Careers</li><li>Newsletter</li><li>Meet Us</li><li>Digital Piracy</li><li>Catalogues</li></ul>
  <address>Lena Marsh<br>48 Hollow Oak Rd.<br>Fairbrook Ohio 43210<br>(555) 014-2298</address>
  <div class="f-social"><span></span><span></span><span></span><span></span><span></span></div>
</footer>
<div class="abs bottom"><div>Privacy Policy &nbsp;Terms of Use &nbsp;Disclaimer &nbsp;Sitemap</div></div>
<svg class="abs totop" viewBox="0 0 46 46"><polyline points="16,26 23,19 30,26" fill="none" stroke="#9fc0ea" stroke-width="2"/></svg>

</body>
</html>
```